Create a Business Card Design Project for a new logistics company

We need a business card designed for a new company in Australia.

Type of business is logistics/trucking.

Medium will be brushed black metal card that can/will be acid etched to a brushed steel silver, acid die cut and two printed colours of our choice which will be white and pantone orange.

We have hopes that the design will be simple, modern and represent with a quick glance what our company does.

Please read instructions carefully in must have box any questions please ask.

If you are interested in this job please look at other job that we have which is very similar with logo and design

Please have a look at the things that can be done with metals cards on google images for inspiration.

Target Market(s)

Men from 20yrs of age to 60yrs of age

Industry/Entity Type

Steel

Requirements
Must have
• Must Have:
- Front of card:

Must use the company logo and name provided as attachment (see below KWR-black-background-cmyk).
Logo grey will be etched, orange and white will be printed on card. Parts of the logo could even be die cut.

The word -Logistics anytime, anywhere- on front etched, printed or die cut.

detail needed on front or back depending on your design layout.

Name
position
email
mobile

all details can be on front if a nice design is etched on the back of card or to keep front simple you can put all detail on back of card, I will leave the lay out to you.

Colours in logo are

Pantone 144 C Orange
Pantone 11-0601 White
Pantone 7539 C Gray
Pantone 426 C Black

However black will be the base of black metal card. Gray will be replaced with the etching in card revealing the silver. Orange and white will be printed on card.

have fun!!
Nice to have
• The file attached called idea is just an example of what can be designed and etched into card. Google has many more idea's for metal business cards.
Should not have
• Please don't clutter the card
No fonts smaller then 7 points

```html
<!DOCTYPE html>
<html lang="en">
<head>
<meta charset="utf-8">
<title>KWR Industries – Business Card</title>
<link rel="stylesheet" href="https://fonts.googleapis.com/css2?family=Saira:wght@400;600&display=swap">
<style>
  :root {
    --backdrop: #d6d6da;
    --card-black: #131313;
    --card-black-edge: #1c1c1c;
    --orange: #f28a1e;
    --white: #f4f4f4;
    --steel: #8a8a8a;
  }
  * { margin: 0; padding: 0; box-sizing: border-box; }
  html, body {
    width: 1200px;
    height: 960px;
    overflow: hidden;
    background: var(--backdrop);
    font-family: "Saira", "Arial Narrow", sans-serif;
  }
  .canvas {
    position: relative;
    width: 1200px;
    height: 960px;
  }
  .card {
    position: absolute;
    left: 240px;
    width: 720px;
    height: 410px;
    background: linear-gradient(160deg, var(--card-black-edge), var(--card-black) 60%);
    box-shadow: 0 14px 30px rgba(0,0,0,0.25);
  }
  .card--front {
    top: 50px;
    border-radius: 0 110px 0 110px;
  }
  .card--back {
    top: 500px;
    border-radius: 110px 0 110px 0;
  }

  /* Front: company wordmark */
  .brand {
    position: absolute;
    left: 80px;
    top: 100px;
    display: flex;
    align-items: center;
    gap: 16px;
  }
  .brand__square {
    width: 22px;
    height: 22px;
    background: var(--orange);
  }
  .brand__name {
    font-weight: 600;
    font-size: 46px;
    letter-spacing: 2px;
    color: var(--orange);
    line-height: 1;
  }

  /* Front: contact block */
  .contact {
    position: absolute;
    right: 60px;
    bottom: 56px;
    display: flex;
    align-items: center;
    gap: 18px;
  }
  .contact__person {
    text-align: right;
    line-height: 1.15;
  }
  .contact__name {
    font-size: 24px;
    font-weight: 400;
    color: var(--orange);
    text-transform: uppercase;
  }
  .contact__role {
    font-size: 22px;
    color: var(--white);
  }
  .contact__divider {
    width: 1px;
    height: 78px;
    background: var(--steel);
  }
  .contact__details {
    font-size: 19px;
    color: var(--white);
    line-height: 1.3;
  }

  /* Back: wordmark and tagline */
  .back-brand {
    position: absolute;
    left: 0;
    right: 0;
    top: 0;
    bottom: 0;
    display: flex;
    flex-direction: column;
    align-items: center;
    justify-content: center;
    gap: 18px;
  }
  .back-brand__mark {
    display: flex;
    align-items: center;
    gap: 20px;
  }
  .back-brand__square {
    width: 30px;
    height: 30px;
    background: var(--orange);
  }
  .back-brand__name {
    font-weight: 600;
    font-size: 72px;
    letter-spacing: 4px;
    line-height: 1;
    color: var(--orange);
  }
  .back-brand__tagline {
    font-size: 20px;
    letter-spacing: 3px;
    color: var(--white);
    text-transform: uppercase;
  }
</style>
</head>
<body>
  <main class="canvas">
    <section class="card card--front" aria-label="Card front">
      <div class="brand">
        <span class="brand__square"></span>
        <span class="brand__name">KWR Industries</span>
      </div>
      <div class="contact">
        <div class="contact__person">
          <p class="contact__name">Alan Pierce</p>
          <p class="contact__role">President</p>
        </div>
        <span class="contact__divider"></span>
        <div class="contact__details">
          <p>alan@kwrfreight.com</p>
          <p>www.kwrfreight.com</p>
          <p>M 0400 555 218</p>
        </div>
      </div>
    </section>

    <section class="card card--back" aria-label="Card back">
      <div class="back-brand">
        <div class="back-brand__mark">
          <span class="back-brand__square"></span>
          <span class="back-brand__name">KWR</span>
        </div>
        <p class="back-brand__tagline">Logistics anytime, anywhere</p>
      </div>
    </section>
  </main>
</body>
</html>
```